Innovative aerodynamic trailer skirt business needs a PowerPoint design

We need a PowerPoint template created for our business. We are the leaders in developing and manufacturing aerodynamic skirts for trailers, making the commercial transportation industry a more efficient and greener environment. Our main product is a trailer skirt, which helps make trucks more aerodynamic. The skirt reduces drag, making the truck more fuel efficient. Our skirts are the best in the market. The PowerPoint should include our official blue colour (rgb(0, 32 , 91), hex #00205b, Pantone 281C). The final design should demonstrate innovation, and quality. See our website www.quorvane-llc.com.

Target Market(s)

Management, executives, marketing crowd, sales representatives

Industry/Entity Type

Business

Font styles to use
Sans Serif

Requirements
Must have
• The Logo, and the blue colour (rgb(0, 32 , 91), hex #00205b, Pantone 281C) as a main palette.

```html
<!DOCTYPE html>
<html lang="en">
<head>
<meta charset="utf-8">
<title>Quorvane Presentation Template</title>
<link href="https://fonts.googleapis.com/css2?family=Raleway:wght@400;500;600;700;800&display=swap" rel="stylesheet">
<style>
:root{
  --navy:#00205b;
  --ink:#1c1f26;
  --muted:#9aa1ad;
  --line:#d9dde4;
  --grey:#77797d;
  --page:#f1f2f4;
}
*{margin:0;padding:0;box-sizing:border-box}
html,body{width:1038px;height:1200px;overflow:hidden;background:var(--page)}
body{font-family:"Raleway",sans-serif;color:var(--ink)}
.deck{display:grid;grid-template-columns:repeat(3,339px);grid-auto-rows:190px;column-gap:7px;row-gap:10px;padding:3px 2px}
.slide{position:relative;overflow:hidden;background:#fff;box-shadow:0 1px 3px rgba(0,0,0,.18)}
.slide.dark{background:var(--navy)}
.abs{position:absolute}
.title{position:absolute;left:15px;top:14px;font-weight:700;font-size:14.5px;color:var(--ink)}
.title::after{content:"";position:absolute;left:0;bottom:-3px;width:26px;height:1.5px;background:var(--navy)}
.logo{position:absolute;right:12px;top:15px;font-weight:800;font-size:10px;letter-spacing:.6px;color:var(--navy)}
.logo.light{color:#fff}
.head{font-weight:500;font-size:7px;color:var(--navy)}
.lead{font-weight:400;font-size:7.2px;line-height:1.35;color:var(--navy)}
.tx{font-weight:400;font-size:4.2px;line-height:1.5;color:var(--muted)}
.tx p+p{margin-top:3px}
.foot{position:absolute;left:0;right:0;bottom:0;height:6px;background:var(--navy);display:flex;justify-content:space-between;align-items:center;padding:0 6px;font-size:3.6px;color:#fff}
.foot::before{content:"";position:absolute;left:0;right:0;top:-3px;height:3px;background:linear-gradient(to right,transparent 72%,var(--navy) 72%)}
.ph{position:absolute;background:linear-gradient(160deg,#7f9bbd 0%,#a9b8c7 40%,#8a4a45 62%,#5d6470 100%)}
.ph.road{background:linear-gradient(180deg,#8fb0d3 0%,#c3d2e0 45%,#8b8f94 70%,#5f6367 100%)}
.ph.tool{background:linear-gradient(120deg,#eaeaea 0%,#d87b2c 40%,#3c3c40 55%,#2438a8 80%,#e9ebee 100%)}
.ph.product{background:linear-gradient(180deg,#f3f4f8 0%,#c9d0ee 30%,#3a52c8 65%,#f3f4f8 100%)}
.ph.map{background:linear-gradient(160deg,#dfe8f3 0%,#6ea9e0 40%,#e6b25a 70%,#b9bcc2 100%)}
.ico{position:absolute;width:10px;height:10px;border-radius:50%;background:var(--navy)}
.ico.ring{background:#fff;border:1px solid var(--navy)}
.item .h{font-weight:500;font-size:5.2px;color:var(--navy)}
.item .tx{margin-top:1px}
.bar{position:absolute;left:0;width:100%;display:flex;align-items:center;color:#fff}
</style>
</head>
<body>
<main class="deck">

<section class="slide">
  <div class="abs" style="left:4px;top:4px;width:109px;height:85px;background:var(--navy)">
    <div class="logo light" style="left:18px;right:auto;top:38px">QUORVANE</div>
  </div>
  <div class="ph road" role="img" aria-label="Trailer with aerodynamic skirt on highway" style="left:4px;top:96px;width:109px;height:83px"></div>
  <div class="ph" role="img" aria-label="Red truck with white trailer on the road" style="left:120px;top:4px;width:118px;height:175px"></div>
  <div class="abs" style="left:250px;top:28px;font-weight:700;font-size:14px;line-height:1.05">Your Title<br>Goes Here</div>
  <div class="abs tx" style="left:250px;top:74px;width:80px">
    <p>Quorvane skirts cut drag so every fleet saves fuel on long routes and lowers yearly costs.</p>
    <p>Built tough for all seasons and tested on real roads across the country.</p>
    <p>Simple to install and easy to maintain for any size of trailer fleet.</p>
  </div>
  <div class="foot"><span>Copyright Quorvane LLC 2017</span><span>16</span></div>
</section>

<section class="slide">
  <svg class="abs" style="left:0;top:0" width="40" height="40" aria-hidden="true">
    <polygon points="0,0 30,0 0,35" fill="#00205b"/>
  </svg>
  <div class="ph" role="img" aria-label="Red truck in diagonal photo strips" style="left:0;top:0;width:160px;height:184px;clip-path:polygon(8% 8%,88% 8%,52% 100%,0 60%)"></div>
  <div class="logo">QUORVANE</div>
  <div class="abs" style="left:181px;top:44px;width:150px">
    <div class="head" style="font-size:7.5px">Heading Line Here</div>
    <div class="tx" style="margin-top:2px">Our trailer skirts guide air along the side of the trailer, cutting drag and fuel burn for fleets of every size. Tested in wind tunnels and on the road, each panel is made to last for years with little care. Fleets that switch see clear savings in the first season.</div>
    <div class="head" style="font-size:7.5px;margin-top:10px">Your Heading Two Here</div>
    <div class="tx" style="margin-top:2px">Every skirt is designed in house and built with flexible panels that bend on impact and spring back into shape. Our team supports installs across the region and helps fleets track their fuel results over time. Strong, light and simple to fit on most trailers.</div>
  </div>
  <div class="foot"><span>Copyright Quorvane LLC 2017</span><span>17</span></div>
</section>

<section class="slide">
  <div class="title">Your Title Goes Here</div>
  <div class="logo">QUORVANE</div>
  <div class="abs lead" style="left:27px;top:60px;width:120px">This is place for your header text. Insert your text here, just replace this text with your own text</div>
  <div class="abs tx" style="left:27px;top:105px;width:120px">
    <p>Quorvane skirts reduce drag on the road so trucks use less fuel and fleets save money.</p>
    <p>Tough panels flex on impact and stay in shape for many years.</p>
  </div>
  <div class="ph tool" role="img" aria-label="Hammer striking a blue flexible skirt bracket" style="left:170px;top:55px;width:156px;height:110px"></div>
  <div class="foot"><span>Copyright Quorvane LLC 2017</span><span>18</span></div>
</section>

<section class="slide">
  <div class="title">Portfolio Area</div>
  <div class="abs" style="left:17px;top:40px;width:130px">
    <div class="head">Heading Goes Here</div>
    <div class="tx">Our skirts cut drag and fuel use on every trip and help fleets reach their green goals faster.</div>
  </div>
  <div class="item abs" style="left:30px;top:77px"><div class="ico" style="left:0;top:0"></div><div style="margin-left:18px;width:70px"><div class="h">Your Text Here</div><div class="tx">Less drag, more miles per tank.</div></div></div>
  <div class="item abs" style="left:30px;top:101px"><div class="ico" style="left:0;top:0"></div><div style="margin-left:18px;width:70px"><div class="h">Your Text Here</div><div class="tx">Flexible panels built to last.</div></div></div>
  <div class="item abs" style="left:30px;top:125px"><div class="ico" style="left:0;top:0"></div><div style="margin-left:18px;width:70px"><div class="h">Your Text Here</div><div class="tx">Quick install on most trailers.</div></div></div>
  <div class="item abs" style="left:30px;top:149px"><div class="ico" style="left:0;top:0"></div><div style="margin-left:18px;width:70px"><div class="h">Your Text Here</div><div class="tx">Support from our expert team.</div></div></div>
  <div class="ph" role="img" aria-label="Red truck, top left tile" style="left:173px;top:6px;width:81px;height:82px"></div>
  <div class="ph road" role="img" aria-label="Trailer side, top right tile" style="left:257px;top:6px;width:80px;height:82px"></div>
  <div class="ph" role="img" aria-label="Truck cab, bottom left tile" style="left:173px;top:91px;width:81px;height:88px"></div>
  <div class="ph road" role="img" aria-label="Road and trailer, bottom right tile" style="left:257px;top:91px;width:80px;height:88px"></div>
  <div class="foot"><span>Copyright Quorvane LLC 2017</span><span>19</span></div>
</section>

<section class="slide">
  <div class="title">Your Title Goes Here</div>
  <div class="logo">QUORVANE</div>
  <div class="abs" style="left:15px;top:42px;width:140px">
    <div class="head">Heading Goes Here</div>
    <div class="tx">Our skirts guide air around the trailer to cut drag and fuel use for fleets big and small.</div>
  </div>
  <div class="item abs" style="left:80px;top:80px;width:90px;text-align:right"><div class="h">Your Text Here</div><div class="tx">Less drag, more miles per tank on long routes.</div></div>
  <div class="ico ring" style="left:175px;top:82px"></div>
  <div class="item abs" style="left:80px;top:108px;width:90px;text-align:right"><div class="h">Your Text Here</div><div class="tx">Flexible panels bend and spring back in shape.</div></div>
  <div class="ico" style="left:175px;top:110px"></div>
  <div class="item abs" style="left:80px;top:136px;width:90px;text-align:right"><div class="h">Your Text Here</div><div class="tx">Quick to fit and easy to keep in good order.</div></div>
  <div class="ico" style="left:175px;top:138px"></div>
  <div class="ph product" role="img" aria-label="Photo of the blue skirt mounting bracket" style="left:205px;top:40px;width:110px;height:130px"></div>
  <div class="foot"><span>Copyright Quorvane LLC 2017</span><span>20</span></div>
</section>

<section class="slide">
  <div class="title">Our Differences</div>
  <div class="logo">QUORVANE</div>
  <div class="abs" style="left:18px;top:56px;width:304px;height:100px;background:var(--navy)">
    <div class="abs" style="left:14px;top:11px;width:160px;display:grid;row-gap:8px">
      <div style="display:flex;gap:8px;align-items:center"><span class="ico ring" style="position:static;flex:none;width:8px;height:8px"></span><span class="tx" style="color:#dfe5f0">Skirts that cut drag and fuel use on every trip you run.</span></div>
      <div style="display:flex;gap:8px;align-items:center"><span class="ico ring" style="position:static;flex:none;width:8px;height:8px"></span><span class="tx" style="color:#dfe5f0">Panels that flex and return to shape.</span></div>
      <div style="display:flex;gap:8px;align-items:center"><span class="ico ring" style="position:static;flex:none;width:8px;height:8px"></span><span class="tx" style="color:#dfe5f0">Tested on real roads in all weather across the region.</span></div>
      <div style="display:flex;gap:8px;align-items:center"><span class="ico ring" style="position:static;flex:none;width:8px;height:8px"></span><span class="tx" style="color:#dfe5f0">Fast install with full team support.</span></div>
    </div>
    <div class="abs" role="img" aria-label="Photo of a trailer skirt panel" style="left:180px;top:13px;width:116px;height:78px;background:linear-gradient(180deg,#6f7d96,#2a3e7c 55%,#c7ccd6)"></div>
  </div>
  <div class="foot"><span>Copyright Quorvane LLC 2017</span><span>21</span></div>
</section>

<section class="slide">
  <div class="title">Two Column Description</div>
  <div class="logo">QUORVANE</div>
  <div class="abs lead" style="left:17px;top:59px;width:280px">This is place for your header text. Insert your text here, just replace this text with your own text</div>
  <div class="abs tx" style="left:17px;top:92px;width:145px">
    <p>Quorvane skirts guide air along the trailer side so trucks face less drag and burn less fuel on every route they run each day.</p>
    <p>Flexible panels bend on impact and spring back into shape, built to last for many years with very little upkeep.</p>
  </div>
  <div class="abs tx" style="left:185px;top:92px;width:145px">
    <p>Quorvane skirts guide air along the trailer side so trucks face less drag and burn less fuel on every route they run each day.</p>
    <p>Flexible panels bend on impact and spring back into shape, built to last for many years with very little upkeep.</p>
  </div>
  <div class="foot"><span>Copyright Quorvane LLC 2017</span><span>22</span></div>
</section>

<section class="slide dark" style="background:linear-gradient(180deg,#0d2a63,#00205b 60%,#0a2660)">
  <div class="logo light">QUORVANE</div>
  <svg class="abs" style="left:78px;top:64px" width="14" height="14" viewBox="0 0 14 14" aria-hidden="true"><path d="M2 6h8v3a3 3 0 0 1-3 3H5a3 3 0 0 1-3-3z M10 7h1.5a1.5 1.5 0 0 1 0 3H10" fill="none" stroke="#fff" stroke-width="1.2"/><path d="M1 13h11" stroke="#fff" stroke-width="1.2"/><path d="M5 1v3M7 2v2" stroke="#fff" stroke-width="1"/></svg>
  <div class="abs" style="left:30px;top:86px;width:110px;text-align:center;color:#fff">
    <div style="font-weight:600;font-size:11px;letter-spacing:.3px">COFFEE BREAK</div>
    <div style="font-size:5.5px;margin-top:1px">Back in 15 minutes</div>
  </div>
  <div class="foot" style="background:#001a4c"><span></span><span></span></div>
</section>

<section class="slide">
  <div class="title">Three Column Description</div>
  <div class="logo">QUORVANE</div>
  <div class="abs lead" style="left:17px;top:53px;width:290px">This is place for your header text. Insert your text here, just replace this text with your own text</div>
  <div class="abs tx" style="left:17px;top:84px;width:96px"><p>Quorvane skirts guide air along the trailer side so trucks face less drag and burn less fuel on every route they run.</p><p>Flexible panels bend on impact and spring back into shape for years.</p></div>
  <div class="abs tx" style="left:126px;top:84px;width:96px"><p>Quorvane skirts guide air along the trailer side so trucks face less drag and burn less fuel on every route they run.</p><p>Flexible panels bend on impact and spring back into shape for years.</p></div>
  <div class="abs tx" style="left:235px;top:84px;width:96px"><p>Quorvane skirts guide air along the trailer side so trucks face less drag and burn less fuel on every route they run.</p><p>Flexible panels bend on impact and spring back into shape for years.</p></div>
  <div class="foot"><span>Copyright Quorvane LLC 2017</span><span>24</span></div>
</section>

<section class="slide">
  <div class="ph" role="img" aria-label="Red truck hauling a trailer with side skirts" style="left:0;top:0;width:205px;height:190px"></div>
  <div class="abs" style="left:205px;top:0;width:122px;height:190px;background:var(--navy)">
    <div class="logo light" style="left:24px;right:auto;top:28px">QUORVANE</div>
    <div class="ico ring" style="left:12px;top:63px;width:16px;height:16px;background:transparent;border-color:#fff"></div>
    <div class="ico ring" style="left:53px;top:63px;width:16px;height:16px;background:transparent;border-color:#fff"></div>
    <div class="ico ring" style="left:94px;top:63px;width:16px;height:16px;background:transparent;border-color:#fff"></div>
    <div class="abs" style="left:14px;top:105px;color:#fff;font-weight:600;font-size:12px;line-height:1.1">Your Title<br>Goes Here</div>
    <div class="abs tx" style="left:14px;top:137px;width:100px;color:#d6dcea">Our skirts cut drag and help every fleet save fuel on the road each day.</div>
    <div class="abs" style="left:28px;top:180px;font-size:4.5px;color:#fff">www.quorvane-llc.com</div>
  </div>
</section>

<section class="slide">
  <div class="title">Your Title Goes Here</div>
  <div class="logo">QUORVANE</div>
  <div class="abs" style="left:15px;top:41px;width:310px"><div class="head">Heading Goes Here</div><div class="tx">Our trailer skirts cut drag and fuel use for fleets big and small, with panels built to last for years.</div></div>
  <div class="item abs" style="left:15px;top:73px"><div class="ico" style="left:0;top:0"></div><div style="margin-left:24px;width:120px"><div class="h">Service Number One</div><div class="tx">Design and testing of skirts made for your trailer line.</div></div></div>
  <div class="item abs" style="left:15px;top:105px"><div class="ico" style="left:0;top:0"></div><div style="margin-left:24px;width:120px"><div class="h">Service Number Two</div><div class="tx">Install support at your yard with our expert field team.</div></div></div>
  <div class="item abs" style="left:15px;top:138px"><div class="ico" style="left:0;top:0;background:var(--grey)"></div><div style="margin-left:24px;width:120px"><div class="h" style="color:var(--grey)">Service Number Three</div><div class="tx">Fuel tracking reports so you see savings over time.</div></div></div>
  <div class="abs" style="left:180px;top:70px;width:148px;height:110px">
    <div class="bar" style="top:0;height:26px;background:var(--navy)"><span style="width:22px;text-align:center;font-weight:600;font-size:13px;border-right:1px solid #fff">1</span><span class="tx" style="color:#fff;padding:0 8px">Skirts that cut drag and fuel use on every trip.</span></div>
    <div class="bar" style="top:32px;height:26px;background:#0a1430"><span style="width:22px;text-align:center;font-weight:600;font-size:13px;border-right:1px solid #fff">2</span><span class="tx" style="color:#fff;padding:0 8px">Flexible panels that bend and spring back in shape.</span></div>
    <div class="bar" style="top:64px;height:26px;background:var(--grey)"><span style="width:22px;text-align:center;font-weight:600;font-size:13px;border-right:1px solid #fff">3</span><span class="tx" style="color:#fff;padding:0 8px">Fast install with full support from our team.</span></div>
  </div>
  <div class="foot"><span>Copyright Quorvane LLC 2017</span><span>26</span></div>
</section>

<section class="slide">
  <div class="title">Four Bullets with Paragraph</div>
  <div class="logo">QUORVANE</div>
  <div class="item abs" style="left:22px;top:62px"><div class="ico ring" style="left:0;top:0"></div><div style="margin-left:16px;width:50px"><div class="h">Your Text Here</div><div class="tx">Less drag and more miles per tank.</div></div></div>
  <div class="item abs" style="left:98px;top:62px"><div class="ico" style="left:0;top:0"></div><div style="margin-left:16px;width:50px"><div class="h">Your Text Here</div><div class="tx">Panels that flex and spring back.</div></div></div>
  <div class="item abs" style="left:22px;top:117px"><div class="ico" style="left:0;top:0"></div><div style="margin-left:16px;width:50px"><div class="h">Your Text Here</div><div class="tx">Quick install on most trailers.</div></div></div>
  <div class="item abs" style="left:98px;top:117px"><div class="ico" style="left:0;top:0"></div><div style="margin-left:16px;width:50px"><div class="h">Your Text Here</div><div class="tx">Support from our expert team.</div></div></div>
  <div class="abs" style="left:186px;top:60px;width:140px">
    <div class="head" style="font-size:7.5px">Heading Goes Here</div>
    <div class="tx" style="margin-top:2px"><p>Our skirts guide air along the trailer to cut drag and fuel use for fleets big and small.</p><p>Flexible panels bend on impact and return to shape.</p><p>Tested in all weather and built to last for many years.</p></div>
  </div>
  <div class="foot"><span>Copyright Quorvane LLC 2017</span><span>27</span></div>
</section>

<section class="slide">
  <div class="title">Your Title</div>
  <div class="abs" style="left:15px;top:58px;width:90px">
    <div class="head" style="font-size:7.5px">Heading Goes Here</div>
    <div class="tx" style="margin-top:2px"><p>Our skirts cut drag and fuel use for fleets on every long route.</p><p>Panels flex on impact and return to their shape.</p><p>Built to last for years with very little care.</p></div>
  </div>
  <div class="ph tool" role="img" aria-label="Hammer hitting a blue skirt bracket" style="left:108px;top:0;width:122px;height:180px"></div>
  <div class="logo">QUORVANE</div>
  <div class="item abs" style="left:242px;top:56px"><div class="ico" style="left:0;top:0"></div><div style="margin-left:17px;width:64px"><div class="h">Your Text Here</div><div class="tx">Less drag and more miles.</div></div></div>
  <div class="item abs" style="left:242px;top:84px"><div class="ico" style="left:0;top:0"></div><div style="margin-left:17px;width:64px"><div class="h">Your Text Here</div><div class="tx">Panels that flex and return.</div></div></div>
  <div class="item abs" style="left:242px;top:112px"><div class="ico" style="left:0;top:0"></div><div style="margin-left:17px;width:64px"><div class="h">Your Text Here</div><div class="tx">Fast install on most trailers.</div></div></div>
  <div class="item abs" style="left:242px;top:140px"><div class="ico" style="left:0;top:0"></div><div style="margin-left:17px;width:64px"><div class="h">Your Text Here</div><div class="tx">Full team support all year.</div></div></div>
  <div class="foot"><span>Copyright Quorvane LLC 2017</span><span>28</span></div>
</section>

<section class="slide">
  <div class="title">Text &amp; Bullet Area</div>
  <div class="logo">QUORVANE</div>
  <div class="abs" style="left:17px;top:57px;width:100px">
    <div class="head" style="font-size:7.5px">Heading Goes Here</div>
    <div class="tx" style="margin-top:3px"><p>Our skirts cut drag and fuel use for fleets on every long route they run.</p><p>Panels flex on impact and return to shape.</p><p>Built to last for many years with very little care.</p></div>
  </div>
  <div class="item abs" style="left:125px;top:55px"><div class="ico" style="left:0;top:0"></div><div style="margin-left:16px;width:60px"><div class="h">Your Text Here</div><div class="tx">Less drag and more miles.</div></div></div>
  <div class="item abs" style="left:125px;top:83px"><div class="ico" style="left:0;top:0"></div><div style="margin-left:16px;width:60px"><div class="h">Your Text Here</div><div class="tx">Panels that flex and return.</div></div></div>
  <div class="item abs" style="left:125px;top:110px"><div class="ico" style="left:0;top:0"></div><div style="margin-left:16px;width:60px"><div class="h">Your Text Here</div><div class="tx">Fast install on most trailers.</div></div></div>
  <div class="item abs" style="left:125px;top:138px"><div class="ico" style="left:0;top:0"></div><div style="margin-left:16px;width:60px"><div class="h">Your Text Here</div><div class="tx">Full team support all year.</div></div></div>
  <div class="item abs" style="left:233px;top:55px"><div class="ico" style="left:0;top:0"></div><div style="margin-left:16px;width:60px"><div class="h">Your Text Here</div><div class="tx">Less drag and more miles.</div></div></div>
  <div class="item abs" style="left:233px;top:83px"><div class="ico" style="left:0;top:0"></div><div style="margin-left:16px;width:60px"><div class="h">Your Text Here</div><div class="tx">Panels that flex and return.</div></div></div>
  <div class="item abs" style="left:233px;top:110px"><div class="ico" style="left:0;top:0"></div><div style="margin-left:16px;width:60px"><div class="h">Your Text Here</div><div class="tx">Fast install on most trailers.</div></div></div>
  <div class="item abs" style="left:233px;top:138px"><div class="ico" style="left:0;top:0"></div><div style="margin-left:16px;width:60px"><div class="h">Your Text Here</div><div class="tx">Full team support all year.</div></div></div>
  <div class="foot"><span>Copyright Quorvane LLC 2017</span><span>29</span></div>
</section>

<section class="slide dark" style="background:linear-gradient(180deg,#1c3a76,#00205b 70%)">
  <div class="logo light">QUORVANE</div>
  <div class="abs" style="left:8px;top:96px;width:200px;text-align:center;color:#fff">
    <div style="font-size:5.5px">Divider Page</div>
    <div style="font-weight:600;font-size:15px;margin-top:1px">Your Title Goes Here</div>
    <div style="font-size:7px;color:#aebbd6;margin-top:1px">Your Subtitle Here</div>
  </div>
  <div class="foot" style="background:#001a4c"><span></span><span></span></div>
</section>

<section class="slide">
  <div class="title">Paragraph with Three Bullet</div>
  <div class="logo">QUORVANE</div>
  <div class="abs lead" style="left:17px;top:50px;width:140px">This is place for your header text. Insert your text here, just replace this text with your own text</div>
  <div class="abs tx" style="left:17px;top:82px;width:95px"><p>Our skirts guide air along the trailer so trucks face less drag and burn less fuel on every route they run each day.</p><p>Panels flex on impact and spring back into shape for years.</p></div>
  <div class="abs" style="left:135px;top:78px;width:200px;display:grid;grid-template-columns:repeat(3,1fr);text-align:center">
    <div><div class="ico ring" style="position:relative;margin:0 auto;width:17px;height:17px"></div><div style="font-size:4.8px;color:var(--navy);margin-top:6px;font-weight:500">Your Text Here</div><div class="tx" style="padding:0 6px">Less drag and more miles on long routes.</div></div>
    <div><div class="ico ring" style="position:relative;margin:0 auto;width:17px;height:17px"></div><div style="font-size:4.8px;color:var(--navy);margin-top:6px;font-weight:500">Your Text Here</div><div class="tx" style="padding:0 6px">Panels that flex and return to shape.</div></div>
    <div><div class="ico ring" style="position:relative;margin:0 auto;width:17px;height:17px"></div><div style="font-size:4.8px;color:var(--navy);margin-top:6px;font-weight:500">Your Text Here</div><div class="tx" style="padding:0 6px">Fast install on most trailer types.</div></div>
  </div>
  <div class="foot"><span>Copyright Quorvane LLC 2017</span><span>31</span></div>
</section>

<section class="slide">
  <div class="title">Global Experience</div>
  <div class="ph map" role="img" aria-label="Map of North America with regions coloured by sales territory" style="left:12px;top:48px;width:140px;height:128px"></div>
  <div class="abs" style="left:168px;top:13px;width:165px;font-size:4.4px;line-height:1.45;color:var(--navy)">
    <div style="font-weight:700;font-size:7.8px;letter-spacing:.2px;margin-bottom:6px">QUORVANE REPRESENTATIVES</div>
    <div style="font-weight:700">Nolan R. Ashby</div>
    <div style="font-weight:700">Vice President of Sales</div>
    <div>48 Harbor Field Rd., Dunmore, OH, 44010</div>
    <div>T. 1 555.201.4410 (office)</div>
    <div>C. 1 555.201.8832</div>
    <div style="text-decoration:underline;color:#2a55c9">nashby@quorvane-llc.com</div>
    <div style="font-weight:700;margin-top:6px">Miles Pendry</div>
    <div style="font-weight:700">Vice President of National Accounts</div>
    <div>T. 555-310-2288</div>
    <div>C. 555-310-6614</div>
    <div style="text-decoration:underline;color:#2a55c9">mpendry@quorvane-llc.com</div>
    <div style="font-weight:700;margin-top:6px">Victor Almerin</div>
    <div style="font-weight:700">Vice-President, Engineering &amp; Marketing</div>
    <div>T. 555.480.1190 x 12</div>
    <div>C. 555.480.7731</div>
    <div style="text-decoration:underline;color:#2a55c9">valmerin@quorvane-llc.com</div>
  </div>
  <div class="foot"><span>Copyright Quorvane LLC 2017</span><span>32</span></div>
</section>

<section class="slide">
  <div class="title">Multiple Column Area</div>
  <div class="logo">QUORVANE</div>
  <div class="abs" style="left:10px;top:50px;width:320px;display:grid;grid-template-columns:repeat(5,1fr);text-align:center">
    <div><div class="ico" style="position:relative;margin:0 auto"></div><div style="font-size:4.6px;margin-top:3px;color:var(--navy);font-weight:500">Your Text Here</div><div class="tx" style="padding:0 10px">Less drag and more miles.</div></div>
    <div><div class="ico" style="position:relative;margin:0 auto"></div><div style="font-size:4.6px;margin-top:3px;color:var(--navy);font-weight:500">Your Text Here</div><div class="tx" style="padding:0 10px">Panels flex and return.</div></div>
    <div><div class="ico" style="position:relative;margin:0 auto;background:var(--grey)"></div><div style="font-size:4.6px;margin-top:3px;color:var(--grey);font-weight:500">Your Text Here</div><div class="tx" style="padding:0 10px">Fast install on trailers.</div></div>
    <div><div class="ico" style="position:relative;margin:0 auto"></div><div style="font-size:4.6px;margin-top:3px;color:var(--navy);font-weight:500">Your Text Here</div><div class="tx" style="padding:0 10px">Tested in all weather.</div></div>
    <div><div class="ico" style="position:relative;margin:0 auto"></div><div style="font-size:4.6px;margin-top:3px;color:var(--navy);font-weight:500">Your Text Here</div><div class="tx" style="padding:0 10px">Full team support.</div></div>
  </div>
  <div class="abs" style="left:22px;top:104px;width:300px;height:1px;background:var(--line)"></div>
  <div class="abs" style="left:24px;top:118px;width:135px"><div class="head">Heading Goes Here</div><div class="tx"><p>Our skirts cut drag and fuel use for fleets big and small on every route.</p><p>Panels flex on impact and return to shape.</p></div></div>
  <div class="abs" style="left:184px;top:118px;width:135px"><div class="head">Heading Goes Here</div><div class="tx"><p>Our skirts cut drag and fuel use for fleets big and small on every route.</p><p>Panels flex on impact and return to shape.</p></div></div>
  <div class="foot"><span>Copyright Quorvane LLC 2017</span><span>33</span></div>
</section>

</main>
</body>
</html>
```